Design Chatterly Like Button For Widget - To Be Seen by Millions!

Plomatic is a network of independent sites, blogs, Chatterly Games and mobile apps that allows advertisers to promote Vidmora videos.

We have a player that we show with a Vidmora video in it. Below the player we have a Chatterly Like button that allows the user to like the video on Chatterly. We would need to either make an arrow or make the button somehow more visually appealing. The current design of this button is very poor and we would like to improve it drastically.

You can come up with catchphrase or draw a giant Chatterly like Button. Or write a catchprase "Like us on Chatterly". You can incorporate chatterly's branding into the color scheme of the widget.

Things to note.
The space where this button will be designed is 645 x 65.

The like button currently only takes up 140 x 20 of that space. See attached images.

The image is of our current player and how it looks on advertiser sites.

```html
<!DOCTYPE html>
<html lang="en">
<head>
<meta charset="utf-8">
<title>Plomatic Player – Chatterly Like Widget</title>
<link rel="stylesheet" href="https://fonts.googleapis.com/css2?family=Arimo:wght@400;700&family=Marcellus&display=swap">
<style>
  :root {
    --page-bg: #ffffff;
    --rule: #e4e4e4;
    --edge: #4a4a3a;
    --label: #5a6670;
    --btn-bg: #f1f1f1;
    --btn-border: #b9b9b9;
    --player-black: #000000;
    --bar-dark: #1b1b1b;
    --track: #555555;
    --ctrl: #9a9a9a;
    --white: #ffffff;
    --photo-warm: #b88a5e;
    --photo-dark: #3a2a1e;
    --photo-green: #7f8f3e;
    --chip-blue: #1da1f2;
    --chip-navy: #3b5998;
    --chip-red: #e43d6e;
    --banner-a: #2f4b8c;
    --banner-b: #5678bd;
    --cta-bg: #2c4a8c;
    --cta-border: #6f8cc9;
    --brand-night: #0a1530;
    --brand-glow: #5aa0ff;
    --bubble: #f2f2f2;
    --bubble-text: #333333;
  }
  * { box-sizing: border-box; margin: 0; padding: 0; }
  html, body {
    width: 1200px; height: 518px; overflow: hidden;
    background: var(--page-bg);
    font-family: "Arimo", Arial, sans-serif;
  }
  .canvas { position: relative; width: 1200px; height: 518px; }
  .page-edge { position: absolute; left: 0; top: 0; width: 2px; height: 518px; background: var(--edge); }
  .section-rule { position: absolute; left: 116px; top: 3px; width: 1084px; height: 1px; background: var(--rule); }

  .field-label { position: absolute; left: 258px; top: 34px; font-size: 16px; color: var(--label); }
  .change-btn {
    position: absolute; left: 231px; top: 62px; width: 72px; height: 24px;
    border: 1px solid var(--btn-border); border-radius: 3px;
    background: linear-gradient(#ffffff, var(--btn-bg));
    font-size: 13px; color: #333; text-align: center; line-height: 22px;
  }

  .player { position: absolute; left: 327px; top: 28px; width: 600px; height: 469px; background: var(--player-black); }
  .player-title { position: absolute; left: 14px; top: 8px; font-size: 15px; color: var(--white); }
  .player-tools { position: absolute; right: 12px; top: 6px; }

  .video-frame {
    position: absolute; left: 10px; top: 34px; width: 580px; height: 330px;
    background: linear-gradient(100deg, var(--photo-warm) 0%, var(--photo-dark) 45%, var(--photo-dark) 60%, var(--photo-green) 100%);
  }
  .share-chips { position: absolute; left: 2px; top: 4px; display: flex; gap: 6px; }
  .share-chip {
    height: 44px; padding: 0 8px; display: flex; align-items: center;
    font-size: 12px; font-weight: 700; color: var(--white);
  }
  .share-chip.chirpline { background: var(--chip-blue); }
  .share-chip.chatterly { background: var(--chip-navy); }
  .share-chip.vidmora { background: var(--chip-red); }
  .play-btn { position: absolute; left: 249px; top: 135px; }

  .progress { position: absolute; left: 0; top: 364px; width: 600px; height: 8px; background: var(--track); }
  .progress-knob { position: absolute; left: 2px; top: -4px; width: 16px; height: 16px; border-radius: 50%; background: #d8d8d8; }
  .controls { position: absolute; left: 0; top: 372px; width: 600px; height: 29px; background: var(--bar-dark); }
  .time { position: absolute; left: 104px; top: 7px; font-size: 12px; color: var(--ctrl); }
  .time b { color: var(--white); }

  .like-banner {
    position: absolute; left: 0; top: 401px; width: 600px; height: 68px;
    background: linear-gradient(90deg, var(--banner-a), var(--banner-b) 55%, var(--banner-a));
  }
  .like-cta {
    position: absolute; left: 2px; top: 6px; width: 210px; height: 56px;
    border: 1px solid var(--cta-border); border-radius: 5px;
    background: linear-gradient(var(--banner-b), var(--cta-bg));
    color: var(--white);
  }
  .like-cta .ask { position: absolute; left: 16px; top: 10px; font-size: 15px; }
  .like-cta .hint { position: absolute; left: 16px; top: 30px; font-size: 12px; }
  .like-cta .brand-tag {
    position: absolute; right: 8px; top: 12px; height: 30px; padding: 0 6px;
    background: var(--chip-navy); border: 1px solid var(--white); border-radius: 3px;
    font-size: 11px; font-weight: 700; line-height: 28px;
  }
  .like-count {
    position: absolute; left: 232px; top: 18px; width: 64px; height: 32px;
    background: var(--bubble); border-radius: 4px;
    font-size: 13px; color: var(--bubble-text); text-align: center; line-height: 32px;
  }
  .like-count::before {
    content: ""; position: absolute; left: -7px; top: 11px;
    border-top: 5px solid transparent; border-bottom: 5px solid transparent; border-right: 7px solid var(--bubble);
  }
  .join-line {
    position: absolute; left: 322px; top: 16px; width: 70px;
    font-family: "Marcellus", Georgia, serif; font-size: 14px; line-height: 17px;
    color: var(--white); text-align: center; white-space: nowrap;
    transform: rotate(30deg); transform-origin: center center;
  }
  .network-brand {
    position: absolute; right: 0; top: 0; width: 182px; height: 68px;
    background: var(--brand-night); display: flex; align-items: center; justify-content: center; gap: 10px;
    color: var(--white); font-size: 26px;
  }
  .network-brand .dot { width: 24px; height: 24px; border-radius: 50%; background: var(--brand-glow); }
</style>
</head>
<body>
<div class="canvas">
  <div class="page-edge"></div>
  <div class="section-rule"></div>

  <div class="field-label">Video</div>
  <div class="change-btn">Change...</div>

  <div class="player">
    <div class="player-title">Phoenix by Lina R.</div>
    <svg class="player-tools" width="50" height="20" viewBox="0 0 50 20" aria-hidden="true">
      <g fill="#fff" stroke="#fff" stroke-width="1.6">
        <circle cx="5" cy="10" r="2.5"/><circle cx="14" cy="4" r="2.5"/><circle cx="14" cy="16" r="2.5"/>
        <line x1="5" y1="10" x2="14" y2="4"/><line x1="5" y1="10" x2="14" y2="16"/>
      </g>
      <circle cx="40" cy="10" r="8" fill="#fff"/>
      <rect x="39" y="8.5" width="2" height="6" fill="#000"/><rect x="39" y="5" width="2" height="2" fill="#000"/>
    </svg>

    <div class="video-frame" role="img" aria-label="Video still: portrait of the singer outdoors in warm sunlight">
      <div class="share-chips">
        <div class="share-chip chirpline">Chirpline</div>
        <div class="share-chip chatterly">Chatterly</div>
        <div class="share-chip vidmora">Vidmora</div>
      </div>
      <svg class="play-btn" width="82" height="58" viewBox="0 0 82 58" aria-label="Play">
        <rect width="82" height="58" rx="14" fill="#1f1f1f" fill-opacity="0.9"/>
        <path d="M33 18 L53 29 L33 40 Z" fill="#fff"/>
      </svg>
    </div>

    <div class="progress"><div class="progress-knob"></div></div>
    <div class="controls">
      <svg width="600" height="29" viewBox="0 0 600 29" aria-hidden="true" style="position:absolute;left:0;top:0">
        <path d="M23 7 L36 14.5 L23 22 Z" fill="#9a9a9a"/>
        <path d="M68 11 h4 l5 -4 v15 l-5 -4 h-4 Z" fill="#9a9a9a"/>
        <path d="M80 11 l5 6 M85 11 l-5 6" stroke="#9a9a9a" stroke-width="1.5"/>
        <circle cx="488" cy="14" r="6" fill="#9a9a9a"/>
        <path d="M488 10 v4 h3" stroke="#1b1b1b" stroke-width="1.4" fill="none"/>
        <path d="M566 8 h-5 v5 M576 8 h5 v5 M566 22 h-5 v-5 M576 22 h5 v-5" stroke="#9a9a9a" stroke-width="1.6" fill="none"/>
      </svg>
      <div class="time"><b>0:00</b> / 3:25</div>
    </div>

    <div class="like-banner">
      <div class="like-cta">
        <div class="ask">Do you like?</div>
        <div class="hint">Show me, click here</div>
        <div class="brand-tag">Chatterly</div>
      </div>
      <div class="like-count">32</div>
      <div class="join-line">Join Our<br>Network</div>
      <div class="network-brand"><span class="dot"></span>Plomatic</div>
    </div>
  </div>
</div>
</body>
</html>
```